Business Card Design Project

Company Name - Kestrova Care

Wellness consulting and training company. Run through a medical centre.

Main colour themes are orange and blue, as in the logo. Want to replicate same effect with business cards.

To give a sense of freedom and potential as per the company name.

Want the business card to be in line with stationary design, which I have launched as well.

Double sided with design and colour on one side and details on other side.
Updates

Reason: Need business card and stationary design to be teed up.

Target Market(s)

35 to 65 age group.
New age and trendy

Industry/Entity Type

Training

Requirements
Must have
• Colours orange and blue as per logo
Nice to have
• Design to be similar to stationary design, letterhead and envelopes

```html
<!DOCTYPE html>
<html lang="en">
<head>
<meta charset="utf-8">
<title>Kestrova Care – Business Card Proposal</title>
<link rel="stylesheet" href="https://fonts.googleapis.com/css2?family=Open+Sans:ital,wght@0,400;1,400&display=swap">
<style>
  :root {
    --board-grey: #b1b1b1;
    --ink: #1d1d1f;
    --brand-blue: #1c6fb8;
    --sky-blue: #8fc0e8;
    --mid-blue: #2a78c2;
    --brand-orange: #e8621a;
    --white: #ffffff;
  }
  * { margin: 0; padding: 0; box-sizing: border-box; }
  html, body {
    width: 1200px;
    height: 907px;
    overflow: hidden;
  }
  body {
    position: relative;
    background: var(--board-grey);
    font-family: "Open Sans", Arial, sans-serif;
    color: var(--ink);
  }

  .card {
    position: absolute;
    left: 73px;
    width: 512px;
    height: 313px;
    overflow: hidden;
  }

  /* Front of card */
  .card--front {
    top: 90px;
    background: linear-gradient(to bottom, var(--sky-blue) 0%, #cfe3f4 45%, var(--white) 62%, var(--white) 100%);
  }
  .card__star-area {
    position: absolute;
    left: 0;
    top: 0;
    width: 370px;
    height: 290px;
    background: radial-gradient(ellipse at 42% 42%, rgba(28,111,184,0.75) 0%, rgba(42,120,194,0.45) 40%, rgba(143,192,232,0) 72%);
  }
  .card__wordmark {
    position: absolute;
    display: flex;
    align-items: center;
    gap: 10px;
    white-space: nowrap;
    font-weight: 400;
    line-height: 1;
  }
  .card--front .card__wordmark {
    right: 28px;
    bottom: 38px;
    font-size: 44px;
    color: var(--brand-blue);
  }
  .card__mark-dot {
    display: block;
    border-radius: 50%;
    background: var(--brand-orange);
    flex: none;
  }
  .card--front .card__mark-dot { width: 22px; height: 22px; }

  /* Back of card */
  .card--back {
    top: 484px;
    background: var(--brand-blue);
    color: var(--white);
  }
  .card--back .card__wordmark {
    left: 28px;
    top: 128px;
    font-size: 34px;
    color: var(--white);
  }
  .card--back .card__mark-dot { width: 16px; height: 16px; }
  .card__tagline {
    position: absolute;
    left: 28px;
    top: 178px;
    font-size: 17px;
    font-style: italic;
  }
  .card__contacts {
    position: absolute;
    left: 28px;
    top: 226px;
    list-style: none;
    font-size: 15px;
    line-height: 20px;
  }

  /* Designer's note */
  .proposal-note {
    position: absolute;
    left: 700px;
    top: 102px;
    width: 480px;
    font-size: 21px;
    font-style: italic;
    letter-spacing: 1.6px;
    line-height: 31.2px;
  }
  .proposal-note p + p { margin-top: 31.2px; }
</style>
</head>
<body>

<section class="card card--front" aria-label="Business card front">
  <div class="card__star-area" role="img" aria-label="Blue star-shaped wheel decoration"></div>
  <div class="card__wordmark">
    <span>Kestrova Care</span>
    <span class="card__mark-dot"></span>
  </div>
</section>

<section class="card card--back" aria-label="Business card back">
  <div class="card__wordmark">
    <span>Kestrova Care</span>
    <span class="card__mark-dot"></span>
  </div>
  <p class="card__tagline">Wellness, Consulting and Training</p>
  <ul class="card__contacts">
    <li>General Email: enquiries@kestrovacare.com</li>
    <li>Daniel Ashworth: Daniel@kestrovacare.com&nbsp; 07700 900412</li>
    <li>Helen Marlowe: Helen@kestrovacare.com 07700 900538</li>
  </ul>
</section>

<article class="proposal-note">
  <p>These are my designs for your<br>new Kestrova Care business cards.</p>
  <p>I have rotated your logo flag to<br>make a wheel / star to show the<br>wheel of life and how you can turn<br>things around though timely medical<br>intervention.</p>
  <p>The back of the card I have made<br>blue with reversed out writing to<br>differentiate it from the sea of white<br>business cards.</p>
  <p>Of course, should you choose my design<br>I can upate the cards for you with the<br>correct names of staff members etc.</p>
  <p>I hope to hear from you soon,</p>
</article>

</body>
</html>
```